Meridel Capra SA Business Cards

Dear all,
Thank you for reading my brief and project. My company is doing doing advisory in real estate and to comapnies + real estates services as asset management, brokerage, development etc.
I would like to get a business card for my company which is clear, professionnal and serious.
Please have a look to the attachement to see the logos of the company

Industry/Entity Type

Real Estate

Contact Information for Business Card

I would like to have in the business card the following
Principal side:
- Logo of the company (or Monogram)
- First and Last Name (Paulo Vestrand)
- Mobile number
- email address

Second side:
- Address (Chemin des Orvets 17, 1226 Thônex - Switzerland)
- website (www.meridelcapra.ch)

Requirements
Must have
• Refer to the typeface and logo colors

```html
<!DOCTYPE html>
<html lang="en">
<head>
<meta charset="utf-8">
<title>Meridel Capra SA – Business Card</title>
<link rel="stylesheet" href="https://fonts.googleapis.com/css2?family=Work+Sans:wght@400;500;600&display=swap">
<style>
  :root {
    --page-bg: #2b2b2d;
    --card-white: #ffffff;
    --brand-blue: #1a72b9;
    --brand-slate: #3d4756;
    --text-ink: #3a3f47;
    --back-light: #1d8db3;
    --back-mid: #125f8d;
    --back-dark: #0b3460;
    --back-text: #ffffff;
  }
  * { box-sizing: border-box; margin: 0; padding: 0; }
  html, body {
    width: 1200px; height: 900px; overflow: hidden;
    background: var(--page-bg);
    font-family: "Work Sans", Arial, sans-serif;
  }
  .canvas { position: relative; width: 1200px; height: 900px; }

  .card {
    position: absolute; left: 261px; width: 656px; height: 357px;
    overflow: hidden;
    box-shadow: 0 4px 14px rgba(0,0,0,0.45);
  }

  /* Front */
  .card-front { top: 69px; background: var(--card-white); color: var(--text-ink); }
  .brand {
    position: absolute; left: 23px; top: 44px;
    display: flex; align-items: center; gap: 12px;
  }
  .brand-dot { width: 22px; height: 22px; border-radius: 50%; background: var(--brand-blue); }
  .brand-name {
    font-size: 18px; font-weight: 600; letter-spacing: 0.3px;
    color: var(--brand-slate); text-transform: uppercase;
  }
  .holder-name {
    position: absolute; right: 30px; top: 178px;
    font-size: 25px; font-weight: 500; color: var(--brand-blue); letter-spacing: 0.5px;
  }
  .holder-rule {
    position: absolute; left: 23px; top: 219px; width: 517px; height: 1px;
    background: var(--brand-blue);
  }
  .holder-role {
    position: absolute; right: 30px; top: 207px;
    font-size: 16px; letter-spacing: 0.8px;
  }
  .contact-list, .address {
    position: absolute; top: 249px; list-style: none;
    font-size: 16px; line-height: 22.5px; letter-spacing: 0.8px;
  }
  .contact-list { left: 23px; }
  .contact-list li { display: flex; align-items: center; gap: 7px; }
  .contact-icon { width: 11px; height: 11px; flex: none; }
  .web-accent { color: var(--brand-blue); }
  .address { right: 30px; text-align: right; }
  .front-footer { position: absolute; left: 0; bottom: 0; width: 656px; height: 30px; display: block; }

  /* Back */
  .card-back { top: 472px; height: 358px; }
  .back-field {
    position: absolute; inset: 0;
    background: radial-gradient(ellipse at 50% 35%, var(--back-light) 0%, var(--back-mid) 55%, var(--back-dark) 100%);
  }
  .back-brand {
    position: absolute; inset: 0;
    display: flex; align-items: center; justify-content: center; gap: 18px;
  }
  .back-brand .brand-dot { width: 34px; height: 34px; background: var(--back-text); }
  .back-brand .brand-name { font-size: 32px; color: var(--back-text); }
</style>
</head>
<body>
<main class="canvas">

  <section class="card card-front" aria-label="Business card front">
    <div class="brand">
      <span class="brand-dot"></span>
      <span class="brand-name">Meridel Capra</span>
    </div>

    <h1 class="holder-name">Paulo Vestrand</h1>
    <div class="holder-rule"></div>
    <p class="holder-role">Principal</p>

    <ul class="contact-list">
      <li>
        <svg class="contact-icon" viewBox="0 0 12 12" aria-hidden="true"><path d="M3 1 L5 3.5 L4 4.8 Q5 7.3 7.2 8 L8.5 7 L11 9 L9.6 11 Q3.5 10.5 1 2.4 Z" fill="var(--brand-blue)"/></svg>
        +41 22 555 0147
      </li>
      <li>
        <svg class="contact-icon" viewBox="0 0 12 12" aria-hidden="true"><rect x="1" y="2.5" width="10" height="7" rx="1" fill="none" stroke="var(--brand-blue)" stroke-width="1.2"/><path d="M1.5 3 L6 6.5 L10.5 3" fill="none" stroke="var(--brand-blue)" stroke-width="1.2"/></svg>
        info@meridelcapra.ch
      </li>
      <li>
        <svg class="contact-icon" viewBox="0 0 12 12" aria-hidden="true"><g fill="none" stroke="var(--brand-blue)" stroke-width="1"><circle cx="6" cy="6" r="5"/><ellipse cx="6" cy="6" rx="2.2" ry="5"/><path d="M1 6 H11 M2 3.5 H10 M2 8.5 H10"/></g></svg>
        <span>www.<span class="web-accent">meridelcapra</span>.ch</span>
      </li>
    </ul>

    <address class="address" style="font-style:normal">
      Chemin des Orvets 17,<br>
      1226 Thônex<br>
      Switzerland
    </address>

    <svg class="front-footer" viewBox="0 0 656 30" preserveAspectRatio="none" aria-hidden="true">
      <path d="M0 17 H360 C382 17 388 3 412 3 H656 V30 H0 Z" fill="var(--brand-slate)"/>
      <path d="M0 10 H378 C370 13 364 15 354 15 H0 Z" fill="var(--brand-blue)"/>
    </svg>
  </section>

  <section class="card card-back" aria-label="Business card back">
    <div class="back-field" role="img" aria-label="Deep teal-blue background with a fine repeating decorative pattern"></div>
    <div class="back-brand">
      <span class="brand-dot"></span>
      <span class="brand-name">Meridel Capra</span>
    </div>
  </section>

</main>
</body>
</html>
```